Executive recruiting firm in need of business card design

Executive recruiting firm looking for a sleek, classy and modern business card design; card itself will be square shape, rounded edges and soft touch paper, our colors are dark blues in the navy color scale, silvers and grays. Reference our website for a better idea of our company's feel and goals at Staffvex.com - our company message is "Employee Engagement Begins at Recruitment" this should be on the card

Industry/Entity Type

Business

```html
<!DOCTYPE html>
<html lang="en">
<head>
<meta charset="utf-8">
<title>Staffvex business card</title>
<link href="https://fonts.googleapis.com/css2?family=Arimo:wght@400;700&display=swap" rel="stylesheet">
<style>
  :root {
    --page: #ffffff;
    --card-front: #e6e6e6;
    --card-back: #ffffff;
    --card-edge: #d2d2d2;
    --navy: #1f2044;
    --ink: #1b1b2e;
    --slate: #6a6b80;
  }
  * { margin: 0; padding: 0; box-sizing: border-box; }
  html, body { width: 1200px; height: 1000px; overflow: hidden; background: var(--page); }
  .canvas { position: relative; width: 1200px; height: 1000px; }

  .card {
    position: absolute;
    top: 280px;
    width: 440px;
    height: 440px;
    border-radius: 24px;
    border: 1px solid var(--card-edge);
  }
  .card--front { left: 150px; background: var(--card-front); }
  .card--back { left: 620px; background: var(--card-back); }

  .brand {
    position: absolute;
    right: 40px;
    bottom: 60px;
    text-align: right;
    font-family: "Arimo", sans-serif;
  }
  .brand__name {
    font-weight: 700;
    font-size: 34px;
    color: var(--navy);
    line-height: 1;
  }
  .brand__message {
    margin-top: 10px;
    font-size: 12px;
    letter-spacing: 0.5px;
    color: var(--slate);
  }

  .person {
    position: absolute;
    left: 60px;
    top: 84px;
    font-family: "Arimo", sans-serif;
    color: var(--ink);
    line-height: 1.1;
  }
  .person__name { font-size: 22px; font-weight: 400; }
  .person__name strong { font-weight: 700; color: var(--navy); }
  .person__role { font-size: 20px; }

  .contact {
    position: absolute;
    left: 126px;
    bottom: 82px;
    list-style: none;
    font-family: "Arimo", sans-serif;
    font-size: 16px;
    color: var(--ink);
  }
  .contact__item { display: flex; align-items: center; gap: 10px; height: 30px; }
  .contact__icon { width: 18px; height: 18px; fill: none; stroke: var(--ink); stroke-width: 1.4; }
</style>
</head>
<body>
<main class="canvas">
  <section class="card card--front" aria-label="Card front">
    <div class="brand">
      <p class="brand__name">Staffvex</p>
      <p class="brand__message">Employee Engagement Begins at Recruitment</p>
    </div>
  </section>

  <section class="card card--back" aria-label="Card back">
    <div class="person">
      <p class="person__name">Loresum <strong>ipsum</strong></p>
      <p class="person__role">Président</p>
    </div>
    <ul class="contact">
      <li class="contact__item">
        <svg class="contact__icon" viewBox="0 0 20 20"><circle cx="10" cy="10" r="8.5"/><path d="M7 5.5l1.6 2.2-1 1.2c.7 1.4 1.8 2.5 3.2 3.2l1.2-1 2.2 1.6-.9 1.6c-3.6-.4-6.5-3.3-6.9-6.9z"/></svg>
        <span>(418)-555-0142</span>
      </li>
      <li class="contact__item">
        <svg class="contact__icon" viewBox="0 0 20 20"><path d="M2 10L10 3l8 7M4.5 8v9h4v-5h3v5h4V8"/></svg>
        <span>www.staffvex.com</span>
      </li>
      <li class="contact__item">
        <svg class="contact__icon" viewBox="0 0 20 20"><rect x="2" y="4.5" width="16" height="11"/><path d="M2 4.5l8 6.5 8-6.5M2 15.5l6-5.5M18 15.5l-6-5.5"/></svg>
        <span>hello@Staffvex.com</span>
      </li>
    </ul>
  </section>
</main>
</body>
</html>
```